Pop punk gig poster design!

In need of an amazing poster design for a gig We are organising, the genre is pop punk, and will be an all ages gig. I need to it bold, random and capture the eye of any bypasses, and make people want to go to the gig just because the poster is awesome! The event will be called "A night of comets" and will consist of three bands and an acoustic set to open. All the bands are full of energy and create an unreal ambiance during there shows, I would like to capture that in the poster. Open to anything spectacular, the sky is the limit.

Requirements
Must have
• I need to have the name of the event "A Night Of Comets"
Band names(in this order):
-Turn the Dial
-Frozen Fenwick
-Wilma's Lantern
-Loralie Pettigrew

Date: Saturday 10th November 2012
Time: 5:15pm
Venue: The Kiln, 47 Tamsin street, West End, QLD 4101
Ticket price: $10+bf online
$15 at the door.
Free BBQ

```html
<!DOCTYPE html>
<html lang="en">
<head>
<meta charset="utf-8">
<title>A Night Of Comets – Gig Poster</title>
<link href="https://fonts.googleapis.com/css2?family=Oswald:wght@500;700&family=Special+Elite&family=Bangers&display=swap" rel="stylesheet">
<style>
  :root {
    --ink: #000000;
    --smoke: #4a4a4a;
    --blood: #b3120f;
    --blood-dark: #7a0a08;
    --volt: #f2ee1c;
    --ember: #e6801f;
  }
  html, body {
    margin: 0;
    padding: 0;
    width: 849px;
    height: 1200px;
    overflow: hidden;
    background: var(--ink);
  }
  .poster {
    display: block;
    width: 849px;
    height: 1200px;
    background: var(--ink);
  }
  .title-lead { font-family: "Oswald", sans-serif; font-weight: 500; fill: var(--volt); }
  .title-word { font-family: "Special Elite", monospace; fill: var(--ink); }
  .title-chip { fill: var(--volt); }
  .band {
    font-family: "Special Elite", monospace;
    fill: var(--volt);
    stroke: var(--blood);
    stroke-width: 6px;
    paint-order: stroke fill;
    stroke-linejoin: round;
  }
  .info { font-family: "Bangers", sans-serif; fill: var(--ember); letter-spacing: 1px; }
  .bbq { font-family: "Oswald", sans-serif; font-weight: 700; fill: var(--blood); }
</style>
</head>
<body>
<svg class="poster" viewBox="0 0 849 1200" xmlns="http://www.w3.org/2000/svg">
  <defs>
    <radialGradient id="emblem-fade" cx="50%" cy="50%" r="50%">
      <stop offset="0%" stop-color="#2a2a2a"/>
      <stop offset="70%" stop-color="#4a4a4a"/>
      <stop offset="100%" stop-color="#000000" stop-opacity="0"/>
    </radialGradient>
    <radialGradient id="badge-fade" cx="50%" cy="50%" r="50%">
      <stop offset="0%" stop-color="#7a0a08"/>
      <stop offset="75%" stop-color="#b3120f"/>
      <stop offset="100%" stop-color="#b3120f" stop-opacity="0"/>
    </radialGradient>
  </defs>

  <rect class="backdrop-emblem" x="0" y="40" width="849" height="1010" fill="url(#emblem-fade)" role="img" aria-label="Large faded grey circled emblem behind the line-up"/>

  <text class="title-lead" x="255" y="112" font-size="64" textLength="330" lengthAdjust="spacingAndGlyphs">A NIGHT OF</text>

  <ellipse class="title-emblem" cx="205" cy="280" rx="190" ry="190" fill="url(#badge-fade)" role="img" aria-label="Red distressed circled emblem leading the title"/>

  <g class="title-ransom">
    <rect class="title-chip" x="365" y="160" width="465" height="120"/>
    <rect class="title-chip" x="700" y="105" width="130" height="70"/>
    <text class="title-word" x="380" y="255" font-size="118" textLength="435" lengthAdjust="spacingAndGlyphs">Comets</text>
  </g>

  <g class="lineup">
    <text class="band" x="122" y="545" font-size="66" textLength="628" lengthAdjust="spacingAndGlyphs">TURN THE DIAL</text>
    <text class="band" x="205" y="618" font-size="54" textLength="595" lengthAdjust="spacingAndGlyphs">FROZEN FENWICK</text>
    <text class="band" x="220" y="694" font-size="58" textLength="580" lengthAdjust="spacingAndGlyphs">WILMA'S LANTERN</text>
    <text class="band" x="310" y="752" font-size="42" textLength="480" lengthAdjust="spacingAndGlyphs">LORALIE PETTIGREW</text>
  </g>

  <g class="details">
    <text class="info" x="435" y="945" font-size="28" textLength="95" lengthAdjust="spacingAndGlyphs">5:15PM</text>
    <text class="info" x="32" y="966" font-size="30" textLength="270" lengthAdjust="spacingAndGlyphs">LIVE AT THE KILN</text>
    <text class="info" x="40" y="1008" font-size="34" textLength="520" lengthAdjust="spacingAndGlyphs">SATURDAY 10TH NOVEMBER 2012</text>
    <text class="info" x="260" y="1050" font-size="28" textLength="455" lengthAdjust="spacingAndGlyphs">TICKET PRICES $10 +BF ONLINE</text>
    <text class="bbq" x="235" y="1114" font-size="48" textLength="222" lengthAdjust="spacingAndGlyphs">FREE BBQ</text>
    <text class="info" x="495" y="1100" font-size="32" textLength="290" lengthAdjust="spacingAndGlyphs">$15 AT THE DOOR</text>
    <text class="info" x="222" y="1160" font-size="26" textLength="588" lengthAdjust="spacingAndGlyphs">THE KILN, 47 TAMSIN STREET, WEST END. QLD 4101</text>
  </g>
</svg>
</body>
</html>
```